Career Ad - Graphic Image to Attract New Team Members to our Company

We would like a career ad to be used for recruiting staff. This ad will be posted through our social media sites and may also be printed on post cards. Concept we like so far (however we are open to other creative ideas) is a photo in the background with printing on top. The color would be our brand color : blue. As for content, words like "We're Hiring" or "Come join our team" we'd also like to have reference to our website https://lindenvale.ca/about/careers and our email careers@lindenvale.ca Of course, our logo and company name, which is attached in the files
Target Market(s)
Professional
Requirements
Must have
- company logo
Nice to have
- visually apealling

```html
<!DOCTYPE html>
<html lang="en">
<head>
<meta charset="utf-8">
<title>Lindenvale Brokers – Careers</title>
<link href="https://fonts.googleapis.com/css2?family=Bebas+Neue&family=Montserrat:wght@400;600&display=swap" rel="stylesheet">
<style>
  :root {
    --brand-light: #4a86c6;
    --brand-mid: #1f62b0;
    --brand-deep: #0a4596;
    --halo: #a9cdf5;
    --halo-soft: #6fa6e4;
    --ring: #bcd9f7;
    --white: #ffffff;
    --ink-blue: #1a5aa8;
  }
  * { margin: 0; padding: 0; box-sizing: border-box; }
  html, body { width: 1200px; height: 1200px; overflow: hidden; background: var(--white); }
  .career-ad {
    position: relative;
    width: 1200px;
    height: 1200px;
    background: linear-gradient(135deg, var(--brand-light) 0%, var(--brand-mid) 45%, var(--brand-deep) 100%);
    color: var(--white);
    font-family: "Montserrat", sans-serif;
    overflow: hidden;
  }
  .brand {
    position: absolute;
    left: 60px;
    top: 56px;
    display: flex;
    align-items: center;
    gap: 14px;
  }
  .brand-dot {
    width: 34px; height: 34px;
    border-radius: 50%;
    background: var(--white);
  }
  .brand-name {
    font-weight: 600;
    font-size: 30px;
    letter-spacing: 2px;
    color: var(--white);
    white-space: nowrap;
  }
  .ring { position: absolute; left: 0; top: 0; }
  .hero-art {
    position: absolute;
    left: 250px;
    top: 230px;
    width: 650px;
    height: 650px;
    border-radius: 50%;
    background: radial-gradient(circle at 50% 45%, var(--halo) 0%, var(--halo) 55%, var(--halo-soft) 100%);
  }
  .hiring-bubble {
    position: absolute;
    left: 660px;
    top: 300px;
    width: 470px;
    height: 150px;
  }
  .hiring-bubble svg { position: absolute; left: 0; top: 0; }
  .hiring-text {
    position: absolute;
    left: 0;
    top: 0;
    width: 470px;
    height: 124px;
    display: flex;
    align-items: center;
    justify-content: center;
    font-family: "Bebas Neue", sans-serif;
    font-size: 84px;
    line-height: 1;
    padding-top: 6px;
    color: var(--ink-blue);
    letter-spacing: 1px;
    white-space: nowrap;
  }
  .tagline {
    position: absolute;
    left: 0;
    width: 1200px;
    top: 905px;
    text-align: center;
    font-family: "Bebas Neue", sans-serif;
    font-weight: 400;
    font-size: 100px;
    letter-spacing: 7px;
    line-height: 1;
    white-space: nowrap;
  }
  .contact-email {
    position: absolute;
    left: 50%;
    top: 1030px;
    transform: translateX(-50%);
    border: 3px solid var(--white);
    padding: 6px 24px;
    font-weight: 600;
    font-size: 30px;
    letter-spacing: 1px;
    white-space: nowrap;
  }
  .contact-url {
    position: absolute;
    left: 0;
    width: 1200px;
    top: 1105px;
    text-align: center;
    font-size: 22px;
    letter-spacing: 3px;
    white-space: nowrap;
  }
</style>
</head>
<body>
  <main class="career-ad">
    <div class="brand">
      <span class="brand-dot"></span>
      <span class="brand-name">LINDENVALE BROKERS</span>
    </div>

    <svg class="ring" width="1200" height="1200" viewBox="0 0 1200 1200" aria-hidden="true">
      <path d="M 200 560 A 375 375 0 0 1 700 195" fill="none" stroke="var(--ring)" stroke-width="6" stroke-linecap="round" opacity="0.8"/>
      <path d="M 950 560 A 375 375 0 0 1 820 840" fill="none" stroke="var(--ring)" stroke-width="6" stroke-linecap="round" opacity="0.8"/>
    </svg>

    <div class="hero-art" role="img" aria-label="Illustration of an empty blue office chair waiting for a new team member"></div>

    <div class="hiring-bubble">
      <svg width="470" height="150" viewBox="0 0 470 150" aria-hidden="true">
        <rect x="0" y="0" width="470" height="124" rx="62" fill="#ffffff"/>
        <path d="M 70 114 L 60 150 L 115 116 Z" fill="#ffffff"/>
      </svg>
      <div class="hiring-text">WE ARE HIRING</div>
    </div>

    <h1 class="tagline">COME JOIN OUR TEAM</h1>
    <div class="contact-email">careers@lindenvale.ca</div>
    <div class="contact-url">https://lindenvale.ca/about/careers</div>
  </main>
</body>
</html>
```